Metal Business Card Design Project

I already use a nice Metal Business card. My new card will have a little bit more info, and I am trying to make it nice.
I will upload the current design suggestion, but need it better.
The metal card can be cut, or written.

This is the info:

Dr. Henrique Tavares Lobo Siqueira
CRM 274390
Cirurgia Vascular e Endovascular
Prof. Assist. de Cirurgia Vascular da Universidade de Vale Florido
dr.henrique@siqueira-exemplo.com.br

Hospital Jorge Valadares:
Tel (11) 3867-4412
Av. Jorge Valadares 318/502
Bloco C3 - 7 andar
Morumbi - São Paulo
http://venosul-exemplo.pro

Siqueira Consultório Médico:
Tel (11) 47283916
Fax (11) 48619072
Av. Sabiá, 287
Moema - São Paulo
http://www.siqueira-exemplo.com.br

Industry/Entity Type

Business

Requirements
Must have
• Use my two logos

```html
<!DOCTYPE html>
<html lang="pt-BR">
<head>
<meta charset="utf-8">
<title>Siqueira Consultório Médico – Cartão de Metal</title>
<link rel="stylesheet" href="https://fonts.googleapis.com/css2?family=Arimo:wght@400;700&family=Pinyon+Script&display=swap">
<style>
  :root {
    --backdrop: #e4e2de;
    --metal-light: #eef0f2;
    --metal-mid: #c9ced4;
    --metal-dark: #a9b0b8;
    --band-light: #9ea6af;
    --band-dark: #737c86;
    --ink: #3a3f45;
    --ink-soft: #5c636b;
    --white: #ffffff;
    --accent: #e07b1a;
  }
  * { margin: 0; padding: 0; box-sizing: border-box; }
  html, body {
    width: 1200px; height: 899px; overflow: hidden;
    background: var(--backdrop);
  }
  .canvas { position: relative; width: 1200px; height: 899px; }
  .card {
    position: absolute; left: 100px; top: 140px;
    width: 1000px; height: 620px;
    font-family: "Arimo", Arial, sans-serif;
    color: var(--ink);
  }
  .card-shape { position: absolute; inset: 0; }
  .brand { position: absolute; left: 44px; top: 14px; color: var(--white); }
  .brand-name { font-size: 66px; font-weight: 700; line-height: 1; letter-spacing: -1px; }
  .brand-tagline { font-size: 26px; font-weight: 400; margin-top: 2px; }
  .doctor {
    position: absolute; left: 40px; top: 200px; width: 380px;
    font-size: 18px; line-height: 23px;
  }
  .doctor-name { font-weight: 700; }
  .location-title {
    font-family: "Pinyon Script", cursive;
    font-size: 30px; line-height: 38px; color: var(--ink);
  }
  .location-lines { font-size: 17px; line-height: 22px; color: var(--ink-soft); }
  .hospital { position: absolute; left: 560px; top: 190px; width: 400px; }
  .clinic { position: absolute; left: 270px; top: 400px; width: 400px; }
  .partner-mark {
    position: absolute; right: 44px; bottom: 34px;
    font-size: 30px; font-weight: 400; letter-spacing: 1px;
    color: var(--white);
  }
</style>
</head>
<body>
<div class="canvas">
  <article class="card">
    <svg class="card-shape" viewBox="0 0 1000 620" width="1000" height="620" aria-hidden="true">
      <defs>
        <linearGradient id="metal" x1="0" y1="0" x2="1" y2="1">
          <stop offset="0" stop-color="var(--metal-light)"/>
          <stop offset="0.5" stop-color="var(--metal-mid)"/>
          <stop offset="1" stop-color="var(--metal-dark)"/>
        </linearGradient>
        <linearGradient id="band" x1="0" y1="0" x2="1" y2="0">
          <stop offset="0" stop-color="var(--band-dark)"/>
          <stop offset="1" stop-color="var(--band-light)"/>
        </linearGradient>
      </defs>
      <rect x="0" y="0" width="1000" height="620" rx="30" fill="url(#metal)"/>
      <path d="M30 0 H970 Q1000 0 1000 30 V70 C780 72 640 118 380 148 C220 166 90 150 0 162 V30 Q0 0 30 0 Z" fill="url(#band)"/>
      <circle cx="590" cy="78" r="40" fill="var(--accent)"/>
      <circle cx="448" cy="300" r="34" fill="var(--backdrop)"/>
    </svg>

    <header class="brand">
      <div class="brand-name">Siqueira</div>
      <div class="brand-tagline">consultório médico</div>
    </header>

    <section class="doctor">
      <div class="doctor-name">Dr. Henrique Tavares Lobo Siqueira</div>
      <div>CRM 274390</div>
      <div>Cirurgia Vascular e Endovascular</div>
      <div>Prof. Assist. de Cirurgia Vascular da</div>
      <div>Universidade de Vale Florido</div>
      <div>dr.henrique@siqueira-exemplo.com.br</div>
    </section>

    <section class="hospital">
      <h2 class="location-title">Hospital Jorge Valadares:</h2>
      <div class="location-lines">
        <div>Tel (11) 3867-4412</div>
        <div>Av. Jorge Valadares 318/502</div>
        <div>Bloco C3 - 7 andar</div>
        <div>Morumbi - São Paulo</div>
        <div>http://venosul-exemplo.pro</div>
      </div>
    </section>

    <section class="clinic">
      <h2 class="location-title">Siqueira Consultório Médico:</h2>
      <div class="location-lines">
        <div>Tel (11) 47283916</div>
        <div>Fax (11) 48619072</div>
        <div>Av. Sabiá, 287</div>
        <div>Moema - São Paulo</div>
        <div>http://www.siqueira-exemplo.com.br</div>
      </div>
    </section>

    <div class="partner-mark">VENOSUL.PRO</div>
  </article>
</div>
</body>
</html>
```